Website for SaaS CRM software

We require a cool website for a new SaaS CRM software. The design needs to be slick and modern. I quite like the look of sites like PostOtter.

The character 'Marla' in the video is the main character which we would like to incorporate on each page if possible. Like the chimp on Postotter website.

'Sign Up Free' button or form to feature throughout the site so we have a strong call to action.

Here is a short video which will give you an idea of the software:
https://clipvault.example/83920417
Password: trelbq

You can login to the user software (backend) for screen grabs and to see what the software is all about:
www.taskloomhq.example
Username: tenant7
Password: tenant7

Please note: The website is for the front end which is where we sell the software and NOT once the user has logged in.

Target Market(s)

Small businesses, freelancers, designers, 1-man businesses

Industry/Entity Type

Software

Requirements
Must have
• 1. Opt-in box for getting started for free:

'Sign up for your Free account'

2. Logos for social media : Fb/Twitter/YouTube/LinkedIn / G+
3. Facebook 'LIKE' button
4.The Navigation Bar should always be on display at the top when scrolling
5. Login button near the Navigation Bar
6. Login page or pop-up should also have 'Forgot Password' link which prompts them to enter their email so a password can be emailed to them.

5 pages & a blog in total. The pages we require are:

HOME
- Heading 'Easy to use small business software'
- Should have a video placeholder and some bullet points or tick marks for key features. The video (from YouTube) should open up on a bigger lightbox and the background greyed out.
- Sign up box to have the fields for First Name, Company Name, Email & Password with a check box for 'I agree with Terms & Conditions'

TOUR
Sub-Navigation bar at the top or side bar with the headings for each module i.e CONTACTS, QUOTES, JOBS, DIARY, SALES, PURCHASES, PRODUCTS, REPORTS
Each module with need to have a placeholder for an image or video and 1 paragraph of text explaining key features. Please see http://postotter.example/features/

See how the Navigation buttons stay visible at all times and changes to the next button when scrolling: http://postotter.example/features/

No side bar on this page.

PRICING
Pricing table of 3 to 4 columns with a button at the bottom. This software is a monthly subscription, so we need to show the $/month for each Plan at the top with the name of the Plan
The plans are:
Bronze: Free
Silver: $20/month
Gold: $40 / month
Platinum: $75 / month

No side bar on this page.

Heading at the bottom: 'No minimum contract. Cancel anytime.'

SUPPORT PAGE
This to a contact form to submit a ticket for tech support. We also need a 2-column list for videos which we will put up. The video open up on a lightbox in bigger size.

No side bar on this page.

CONTACT
Contact details i.e name, address, telephone, email & a contact form
No side bar on this page.

BLOG
Pagecraft blog. I love the way the headings, paragraph, font, line spacing, colours are on the PostOtter blog.

Need a side bar.

```html
<!DOCTYPE html>
<html lang="en">
<head>
<meta charset="utf-8">
<title>Taskloom — Pricing</title>
<link rel="stylesheet" href="https://fonts.googleapis.com/css2?family=Arimo:wght@400;700&family=Open+Sans:wght@400&display=swap">
<style>
:root{
  --page:#f2f2f2;
  --band:#dcdcdc;
  --panel:#f5f5f5;
  --footer:#000;
  --blue:#29a3e6;
  --ink:#333;
  --muted:#666;
  --feature:#acacac;
  --cell:#e4e4e4;
  --bronze-a:#7e3f16;--bronze-b:#b9662c;
  --silver-a:#8f8f8f;--silver-b:#b0b0b0;
  --gold-a:#d3a418;--gold-b:#e8c040;
  --plat-a:#f04f0c;--plat-b:#f79a1a;
  --btn-a:#5a5a5a;--btn-b:#2e2e2e;
  --red-a:#f2492e;--red-b:#c41f10;
  --tick:#3c8c1e;--cross:#c0161c;
}
*{box-sizing:border-box;margin:0;padding:0}
html,body{width:1200px;height:681px;overflow:hidden}
body{position:relative;background:var(--page);font-family:Arimo,Arial,sans-serif;color:var(--ink)}
.band{position:absolute;left:0;top:196px;width:1200px;height:392px;background:var(--band);border-top:1px solid #fff}
.topbar{position:absolute;top:7px;left:716px;display:flex;align-items:center;gap:6px}
.login{width:40px;height:14px;background:var(--blue);color:#fff;font-size:8px;line-height:14px;text-align:center;border-radius:2px;margin-right:22px}
.social{display:flex;gap:3px}
.social span{width:12px;height:12px;background:#555;display:block}
.like{height:13px;padding:0 4px 0 14px;border:1px solid #aaa;background:#fff;font-size:8px;line-height:11px;position:relative;border-radius:2px}
.like::before{content:"";position:absolute;left:3px;top:2px;width:7px;height:7px;background:#6b7fa8}
.brand{position:absolute;left:318px;top:44px;display:flex;align-items:center;gap:6px;font-weight:700;font-size:34px;color:#111;letter-spacing:-1px}
.brand i{width:12px;height:12px;border-radius:50%;background:var(--blue);display:block}
.nav{position:absolute;left:558px;top:45px;width:324px;height:35px;background:#fafafa;display:flex;justify-content:space-around;align-items:center;padding:0 6px}
.nav a{font-size:10px;font-weight:700;color:#333;text-decoration:none;position:relative}
.nav a.active::after{content:"";position:absolute;left:0;right:0;bottom:-16px;height:1px;background:#999}
h1{position:absolute;left:318px;top:100px;font-size:40px;font-weight:700;color:var(--blue);letter-spacing:-.5px}
.panel{position:absolute;left:318px;top:160px;width:564px;height:428px;background:var(--panel);border-radius:4px 4px 0 0}
.col{position:absolute;top:216px;width:118px;display:flex;flex-direction:column;font-size:8px;color:#555;text-align:center}
.col .head{height:42px;color:#fff;font-weight:700;line-height:1}
.col .cell{height:24.85px;line-height:24.85px;background:var(--cell);border-bottom:1px solid #f4f4f4}
.col .foot{height:49px;background:var(--cell);display:flex;align-items:center;justify-content:center}
.col .name{font-size:11px;padding-top:6px}
.col .price{font-size:24px;letter-spacing:-1px}
.col .price sup{font-size:13px;vertical-align:8px}
.col .price small{font-size:8px;letter-spacing:0}
.features{left:328px;width:71px}
.features .head{background:#fff;color:var(--muted);font-size:11px;padding-top:9px;line-height:12px;border:1px solid #ddd;border-bottom:0}
.features .cell{background:var(--feature);color:#fff;text-align:left;padding-left:12px;border-bottom:1px solid #c8c8c8}
.features .foot{background:var(--feature)}
.bronze{left:399px}
.bronze .head{background:linear-gradient(var(--bronze-a),var(--bronze-b))}
.silver{left:517px}
.silver .head{background:linear-gradient(var(--silver-a),var(--silver-b))}
.gold{left:754px}
.gold .head{background:linear-gradient(var(--gold-b),var(--gold-a))}
.bronze,.silver{border-left:1px solid #d0d0d0}
.platinum{left:635px;top:206px;width:119px;background:#fff;box-shadow:0 1px 4px rgba(0,0,0,.35);z-index:2}
.platinum .head{height:54px;background:linear-gradient(var(--plat-a),var(--plat-b));clip-path:polygon(0 0,100% 0,100% 80%,50% 100%,0 80%);padding-top:1px}
.platinum .cell{background:#fff;border-bottom:1px solid #ddd}
.platinum .cell:first-of-type{height:22px;line-height:16px}
.platinum .foot{background:#fff;height:56px}
.btn{width:84px;height:22px;border-radius:11px;background:linear-gradient(var(--btn-a),var(--btn-b));color:#fff;font-size:11px;font-weight:700;line-height:22px;box-shadow:0 1px 2px rgba(0,0,0,.4)}
.btn.hot{background:linear-gradient(var(--red-a),var(--red-b))}
.cell svg{vertical-align:middle}
.tagline{position:absolute;left:318px;top:517px;width:564px;text-align:center;font-family:"Open Sans",Verdana,sans-serif;font-size:24px;color:#444}
footer{position:absolute;left:0;top:588px;width:1200px;height:93px;background:var(--footer);color:#fff}
.foot-links{position:absolute;left:318px;top:30px;display:flex;gap:7px;font-size:8px}
.follow{position:absolute;left:786px;top:27px;font-size:8px}
.follow .social{margin-top:4px;gap:6px}
.follow .social span{width:15px;height:14px;background:#555}
</style>
</head>
<body>
<div class="band"></div>

<div class="topbar">
  <div class="login">Login</div>
  <div class="social"><span></span><span></span><span></span><span></span><span></span></div>
  <div class="like">Like</div>
</div>

<div class="brand">Taskloom<i></i></div>

<nav class="nav">
  <a href="#">Home</a><a href="#">Tour</a><a href="#" class="active">Pricing</a><a href="#">Support</a><a href="#">Contact</a><a href="#">Blog</a>
</nav>

<h1>Pricing</h1>

<div class="panel"></div>

<div class="col features">
  <div class="head">Package<br>Features</div>
  <div class="cell">Lorem Ipsum</div><div class="cell">Lorem Ipsum</div><div class="cell">Lorem Ipsum</div><div class="cell">Lorem Ipsum</div><div class="cell">Lorem Ipsum</div><div class="cell">Lorem Ipsum</div><div class="cell">Lorem Ipsum</div>
  <div class="foot"></div>
</div>

<div class="col bronze">
  <div class="head"><div class="name">Bronze Package</div><div class="price">Free</div></div>
  <div class="cell">Lorem Ipsum</div><div class="cell">Lorem Ipsum</div><div class="cell">Lorem Ipsum</div><div class="cell">Lorem Ipsum</div><div class="cell">Lorem ipsum</div><div class="cell">Lorem Ipsum</div>
  <div class="cell"><svg width="9" height="9" viewBox="0 0 9 9"><path d="M1 1L8 8M8 1L1 8" stroke="var(--cross)" stroke-width="2.4"/></svg></div>
  <div class="foot"><div class="btn">SIGN UP</div></div>
</div>

<div class="col silver">
  <div class="head"><div class="name" style="font-size:12px;padding-top:4px">Silver Package</div><div class="price"><sup>$</sup>20<small>/mo</small></div></div>
  <div class="cell">Lorem Ipsum</div><div class="cell">Lorem Ipsum</div><div class="cell">Lorem Ipsum</div><div class="cell">Lorem Ipsum</div><div class="cell">Lorem Ipsum</div><div class="cell">--</div>
  <div class="cell"><svg width="9" height="9" viewBox="0 0 9 9"><path d="M1 1L8 8M8 1L1 8" stroke="var(--cross)" stroke-width="2.4"/></svg></div>
  <div class="foot"><div class="btn">SIGN UP</div></div>
</div>

<div class="col platinum">
  <div class="head"><div class="name" style="font-size:10px;padding-top:5px">Platinum Package</div><div class="price" style="font-size:28px"><sup>$</sup>75<small style="font-size:12px">/mo</small></div></div>
  <div class="cell">Unlimited</div><div class="cell">Unlimited Space</div><div class="cell">Lorem Ipsum</div><div class="cell">Lorem Ipsum</div><div class="cell">500 Email Accounts</div><div class="cell">10 FREE</div>
  <div class="cell"><svg width="12" height="10" viewBox="0 0 12 10"><path d="M1 5L4.5 8.5L11 1.5" fill="none" stroke="var(--tick)" stroke-width="2.6"/></svg></div>
  <div class="foot"><div class="btn hot">SIGN UP</div></div>
</div>

<div class="col gold">
  <div class="head"><div class="name" style="font-size:10px;padding-top:9px">Gold Package</div><div class="price"><sup>$</sup>40<small>/mo</small></div></div>
  <div class="cell">Unlimited</div><div class="cell">30 Gb Space</div><div class="cell">Lorem Ipsum</div><div class="cell">Lorem Ipsum</div><div class="cell">1000 Email Accounts</div><div class="cell">5 FREE</div>
  <div class="cell"><svg width="12" height="10" viewBox="0 0 12 10"><path d="M1 5L4.5 8.5L11 1.5" fill="none" stroke="var(--tick)" stroke-width="2.6"/></svg></div>
  <div class="foot"><div class="btn">SIGN UP</div></div>
</div>

<p class="tagline">No minimum contract. Cancel anytime</p>

<footer>
  <div class="foot-links"><span>Home</span><span>Tour</span><span>Pricing</span><span>Support</span><span>Contact</span><span>Blog</span></div>
  <div class="follow">Follow us
    <div class="social"><span></span><span></span><span></span><span></span><span></span></div>
  </div>
</footer>
</body>
</html>
```